New Business Card Design Project

We require a business card design for Zelvaquin, a newly established Indian company.
Our focus is on the development, manufacturing, and export of a diverse array of pharmaceutical products on a global scale. The card should convey a professional appearance, as our primary markets are in Africa, China, and Southeast Asian nations.
We envision a two-sided business card, with the reverse side dedicated to a logo set against a solid color or an elegantly designed pattern. The corners should be rounded. We would appreciate seeing both horizontal and vertical design options. We trust the designer to utilize their expertise in creating this design.

The content for the business card is included in the attached Word file.

Target Market(s)

Our primary markets are in Africa, China, and Southeast Asian, Latin America, Maldives, Sri Lanka

Industry/Entity Type

Pharmaceutical Manufacturing and Export

Contact Information for Business Card

Colors

Designer to choose colors to be used in the design.

Requirements
Must have
• The reverse side of the business card features solely the logo along with the tagline, "Care for Every Day."
Should not have
• The logo should not exceed two instances, encompassing both the front and back sides of the card.

```html
<!DOCTYPE html>
<html lang="en">
<head>
<meta charset="utf-8">
<title>Zelvaquin Business Card</title>
<link rel="stylesheet" href="https://fonts.googleapis.com/css2?family=Montserrat:wght@700&family=Arimo:wght@400;700&display=swap">
<style>
  :root {
    --stage: #3d3d3d;
    --card-white: #ffffff;
    --brand-blue: #29a9e1;
    --brand-blue-deep: #1f95cf;
    --brand-red: #ef5f4c;
    --ink: #3a3a3a;
    --rule: #cfcfcf;
  }
  * { margin: 0; padding: 0; box-sizing: border-box; }
  html, body { width: 1200px; height: 803px; overflow: hidden; background: var(--stage); }
  .stage {
    position: relative; width: 1200px; height: 803px;
    display: flex; align-items: center; justify-content: center; gap: 40px;
  }
  .card {
    position: relative; width: 530px; height: 303px;
    border-radius: 22px; overflow: hidden;
    box-shadow: 0 14px 30px rgba(0,0,0,0.35);
  }
  /* Front */
  .card--front { background: var(--card-white); }
  .front__brand {
    position: absolute; left: 0; top: 0; width: 265px; height: 270px;
    display: flex; align-items: center; justify-content: center; gap: 10px;
  }
  .brand__dot { width: 16px; height: 16px; border-radius: 50%; background: var(--brand-red); flex: none; }
  .brand__name {
    font-family: "Montserrat", sans-serif; font-weight: 700; font-size: 36px;
    color: var(--brand-blue); letter-spacing: 0.5px; white-space: nowrap;
  }
  .front__divider {
    position: absolute; left: 265px; top: 60px; width: 1px; height: 150px;
    background: linear-gradient(to bottom, transparent, var(--rule) 20%, var(--rule) 80%, transparent);
  }
  .front__info {
    position: absolute; left: 290px; top: 58px; width: 230px;
    font-family: "Arimo", sans-serif; color: var(--ink);
  }
  .info__name { font-weight: 700; font-size: 20px; color: var(--brand-blue); line-height: 1.1; }
  .info__role { font-size: 11px; color: var(--brand-red); margin-top: 2px; }
  .info__address { font-size: 11.5px; line-height: 1.4; margin-top: 16px; }
  .info__contacts { list-style: none; margin-top: 12px; font-size: 11.5px; line-height: 1.55; }
  .info__contacts li { display: flex; align-items: center; gap: 7px; }
  .info__contacts svg { width: 10px; height: 10px; flex: none; }
  .front__band { position: absolute; left: 0; bottom: 0; width: 530px; height: 40px; }
  .band__url {
    position: absolute; right: 26px; bottom: 9px;
    font-family: "Arimo", sans-serif; font-size: 12px; color: #fff; letter-spacing: 0.3px;
  }
  /* Back */
  .card--back {
    background: var(--brand-blue);
    display: flex; flex-direction: column; align-items: center; justify-content: center;
  }
  .back__brand { display: flex; align-items: center; gap: 12px; }
  .back__brand .brand__dot { background: rgba(255,255,255,0.45); width: 18px; height: 18px; }
  .back__brand .brand__name { color: #ffffff; font-size: 40px; }
  .back__tagline {
    margin-top: 22px; font-family: "Arimo", sans-serif; font-size: 14px;
    color: #ffffff; letter-spacing: 0.4px;
  }
</style>
</head>
<body>
<main class="stage">
  <section class="card card--front" aria-label="Card front">
    <div class="front__brand">
      <span class="brand__dot"></span>
      <span class="brand__name">Zelvaquin</span>
    </div>
    <div class="front__divider"></div>
    <div class="front__info">
      <p class="info__name">Rohan K. Desai</p>
      <p class="info__role">CEO</p>
      <p class="info__address">12, Nilgiri Colony, Nashik<br>422005, India</p>
      <ul class="info__contacts">
        <li>
          <svg viewBox="0 0 10 10"><path d="M2 1 L4 1 L4.6 3 L3.6 3.8 Q4.6 5.8 6.2 6.4 L7 5.4 L9 6 L9 8 Q4 9 1 2 Z" fill="var(--brand-blue)"/></svg>
          +919812045730
        </li>
        <li>
          <svg viewBox="0 0 10 10"><rect x="0.5" y="2" width="9" height="6" fill="var(--brand-blue)"/><path d="M0.5 2 L5 5.5 L9.5 2" stroke="#fff" stroke-width="0.9" fill="none"/></svg>
          rdesai@zelvaquin.com
        </li>
        <li>
          <svg viewBox="0 0 10 10"><circle cx="5" cy="5" r="4.5" fill="var(--brand-blue)"/><path d="M0.5 5 H9.5 M5 0.5 Q2.5 5 5 9.5 M5 0.5 Q7.5 5 5 9.5" stroke="#fff" stroke-width="0.6" fill="none"/></svg>
          www.zelvaquin.com
        </li>
      </ul>
    </div>
    <svg class="front__band" viewBox="0 0 530 40" preserveAspectRatio="none" aria-hidden="true">
      <rect x="0" y="32" width="340" height="8" fill="var(--brand-red)"/>
      <polygon points="336,40 348,8 530,8 530,40" fill="var(--brand-blue)"/>
    </svg>
    <span class="band__url">www.zelvaquin.com</span>
  </section>

  <section class="card card--back" aria-label="Card back">
    <div class="back__brand">
      <span class="brand__dot"></span>
      <span class="brand__name">Zelvaquin</span>
    </div>
    <p class="back__tagline">Care for Every Day</p>
  </section>
</main>
</body>
</html>
```